Brightwell Homes Guide Business card

I have had at the logo designed here and attached. The business compares off the plan apartments in Sydney and provides quick comparison for new home buyers e.g price, floor plans and location. I would like the complimentary colours used on the business card. I would like it be unique but also look professional. I also have a website to gain inspiration from www.brightwellhomesguide.com.au
Updates
Industry/Entity Type
Business
Contact Information for Business Card
Helen Vostrakis
Director of Business Development
e: helen.vostrakis@brightwellhomesguide.com.au
p: (02) 8143 7692
m: 0431 572 908
w: www.brightwellhomesguide.com.au
Look and feel
Each slider illustrates characteristics of the customer's brand and the style your logo design should communicate.

```html
<!DOCTYPE html>
<html lang="en">
<head>
<meta charset="utf-8">
<title>Brightwell Homes Guide – Business Card</title>
<link href="https://fonts.googleapis.com/css2?family=Source+Sans+3:wght@400;600;700&display=swap" rel="stylesheet">
<style>
  :root{
    --backdrop:#4a423e;
    --card:#0e0e0e;
    --card-edge:#1c1c1c;
    --green:#7dc443;
    --blue:#1f8fd6;
    --white:#f2f2f2;
    --silver:#d9d9d9;
    --divider:#2a2a2a;
  }
  *{box-sizing:border-box;margin:0;padding:0}
  html,body{width:1200px;height:900px;overflow:hidden}
  body{
    background:var(--backdrop);
    font-family:"Source Sans 3",Arial,sans-serif;
    position:relative;
  }
  .card{
    position:absolute;
    top:295px;
    width:540px;height:310px;
    background:var(--card);
    border:1px solid var(--card-edge);
    border-radius:3px;
    box-shadow:0 10px 28px rgba(0,0,0,.45);
    overflow:hidden;
  }
  .card--front{left:45px}
  .card--back{left:615px;display:flex;align-items:center;justify-content:center}

  .brand{
    display:flex;align-items:center;gap:10px;
    font-weight:600;
    line-height:1.05;
  }
  .brand__mark{width:22px;height:22px;flex:none}
  .card--front .brand{
    position:absolute;left:26px;top:170px;
    width:170px;
    font-size:22px;color:var(--green);
  }
  .card--front .brand__mark{background:var(--blue)}
  .card--back .brand{font-size:36px;color:var(--silver)}
  .card--back .brand__mark{width:34px;height:34px;background:var(--silver)}

  .divider{
    position:absolute;left:210px;top:110px;
    width:1px;height:140px;background:var(--divider);
  }
  .details{
    position:absolute;left:228px;top:52px;right:14px;
    color:var(--white);font-size:14px;line-height:1.3;
  }
  .details__name{color:var(--green);font-weight:700;font-size:17px}
  .details__address{margin-top:14px}
  .contact{list-style:none;margin-top:14px;font-size:12.5px}
  .contact li{display:flex;align-items:center;gap:7px;margin-bottom:2px;white-space:nowrap}
  .contact svg{width:10px;height:10px;flex:none}
</style>
</head>
<body>
  <section class="card card--front" aria-label="Business card front">
    <div class="brand">
      <span class="brand__mark"></span>
      <span class="brand__name">Brightwell Homes Guide</span>
    </div>
    <div class="divider"></div>
    <div class="details">
      <p class="details__name">Helen Vostrakis</p>
      <p class="details__title">Director of Business Development</p>
      <p class="details__address">Level 4, 88 Harbour Street<br>Sydney NSW 2000</p>
      <ul class="contact">
        <li>
          <svg viewBox="0 0 10 10" aria-hidden="true"><path d="M1 3.5C1 2 2 1.5 5 1.5S9 2 9 3.5L7.5 4 7 3H3L2.5 4ZM2.5 5h5L8 8.5H2Z" fill="var(--green)"/></svg>
          (02) 8143 7692
        </li>
        <li>
          <svg viewBox="0 0 10 10" aria-hidden="true"><rect x="2.5" y="0.5" width="5" height="9" rx="1" fill="var(--green)"/><rect x="3.5" y="1.8" width="3" height="5" fill="var(--card)"/></svg>
          0431 572 908
        </li>
        <li>
          <svg viewBox="0 0 10 10" aria-hidden="true"><rect x="0.5" y="2" width="9" height="6.5" fill="var(--green)"/><path d="M0.5 2 5 5.8 9.5 2" stroke="var(--card)" fill="none" stroke-width="1"/></svg>
          helen.vostrakis@brightwellhomesguide.com.au
        </li>
        <li>
          <svg viewBox="0 0 10 10" aria-hidden="true"><g fill="none" stroke="var(--green)" stroke-width="1.4"><rect x="1" y="4.5" width="4.5" height="3" rx="1.5" transform="rotate(-45 3.25 6)"/><rect x="4.5" y="2.5" width="4.5" height="3" rx="1.5" transform="rotate(-45 6.75 4)"/></g></svg>
          www.brightwellhomesguide.com.au
        </li>
      </ul>
    </div>
  </section>

  <section class="card card--back" aria-label="Business card back">
    <div class="brand">
      <span class="brand__mark"></span>
      <span class="brand__name">Brightwell Homes Guide</span>
    </div>
  </section>
</body>
</html>
```